business card for a shoe shop

we would like a business card for a family owned shoe shop.
With this information included.
Darnell's Shoe Store
Family owned since 1947

then on other side
Darnell's Shoe Store
Footwear fitting specialist
Phone: 9187 2630
218 Quarry St, Fernleigh Downs 3187
(cnr. Hartwick Rd and Quarry St)
darnellshoes218@examplemail.com
if could incorporate the purple color on card i have attached.

```html
<!DOCTYPE html>
<html lang="en">
<head>
<meta charset="utf-8">
<title>Darnell's Shoe Store — Business Card</title>
<link rel="stylesheet" href="https://fonts.googleapis.com/css2?family=Inter:wght@400;700&display=swap">
<style>
  :root {
    --stage: #2f2f2f;
    --brand-purple: #8247ff;
    --card-white: #ffffff;
    --ink: #3a3a3a;
    --on-purple: #ffffff;
  }
  * { box-sizing: border-box; margin: 0; padding: 0; }
  html, body { width: 1200px; height: 800px; overflow: hidden; }
  body {
    background: var(--stage);
    font-family: "Inter", Arial, sans-serif;
    display: flex;
    align-items: center;
    justify-content: center;
    gap: 40px;
  }
  .card {
    width: 525px;
    height: 300px;
    border-radius: 22px;
    position: relative;
    overflow: hidden;
  }
  .card--info { background: var(--card-white); display: flex; align-items: center; }
  .card--brand {
    background: var(--brand-purple);
    display: flex; flex-direction: column; justify-content: center; align-items: center;
    color: var(--on-purple);
  }
  .identity { width: 275px; padding-left: 34px; }
  .identity__name {
    font-weight: 700; color: var(--brand-purple);
    font-size: 24px; letter-spacing: -0.3px; line-height: 1.1;
  }
  .identity__tagline { font-size: 13px; color: var(--ink); margin-top: 3px; }
  .divider {
    width: 1px; height: 92px;
    background: linear-gradient(to bottom, transparent, var(--brand-purple) 40%, var(--brand-purple) 60%, transparent);
    margin-right: 22px;
  }
  .contact { list-style: none; font-size: 11.5px; color: var(--ink); line-height: 1.35; }
  .contact__item { display: flex; gap: 8px; align-items: flex-start; margin-bottom: 2px; }
  .contact__icon { width: 11px; height: 11px; flex: none; margin-top: 2px; fill: var(--brand-purple); }
  .brand-block { text-align: left; }
  .brand-block__name { font-weight: 700; font-size: 44px; letter-spacing: -0.6px; line-height: 1; }
  .brand-block__tagline { font-size: 22px; margin-top: 4px; padding-left: 150px; }
</style>
</head>
<body>
  <section class="card card--info" aria-label="Card back with contact details">
    <div class="identity">
      <p class="identity__name">Darnell's Shoe Store</p>
      <p class="identity__tagline">Footwear fitting specialist</p>
    </div>
    <div class="divider"></div>
    <ul class="contact">
      <li class="contact__item">
        <svg class="contact__icon" viewBox="0 0 12 12" aria-hidden="true"><path d="M6 0a4.2 4.2 0 0 0-4.2 4.2C1.8 7.4 6 12 6 12s4.2-4.6 4.2-7.8A4.2 4.2 0 0 0 6 0zm0 5.9a1.7 1.7 0 1 1 0-3.4 1.7 1.7 0 0 1 0 3.4z"/></svg>
        <span>218 Quarry St,<br>Fernleigh Downs 3187<br>(cnr. Hartwick Rd and Quarry St)</span>
      </li>
      <li class="contact__item">
        <svg class="contact__icon" viewBox="0 0 12 12" aria-hidden="true"><path d="M2.4.5l2 2.3-1 1.4a7 7 0 0 0 4.4 4.4l1.4-1 2.3 2-1 1.9C5.3 11.5.5 6.7.5 1.5z"/></svg>
        <span>9187 2630</span>
      </li>
      <li class="contact__item">
        <svg class="contact__icon" viewBox="0 0 12 12" aria-hidden="true"><path d="M0 2h12v8H0zm1 1v.3l5 3.2 5-3.2V3z"/></svg>
        <span>darnellshoes218@examplemail.com</span>
      </li>
    </ul>
  </section>

  <section class="card card--brand" aria-label="Card front">
    <div class="brand-block">
      <p class="brand-block__name">Darnell's Shoe Store</p>
      <p class="brand-block__tagline">Family owned since 1947</p>
    </div>
  </section>
</body>
</html>
```